Design business cards for Ironvale Barbers (Opening March so won't need finalised till January2018

Ironvale Barbers is the new age barbers and skincare for all men. Creating tailor made haircuts & customised skincare solutions for the perfect healthy manly look. The Barbers will have a industrial, rustic, worldly feel about it. Rustic red brick wall with old wine barrels as the work stations with the old fashion barber chairs. Concrete floor and a bit corrugated iron around.
Target Market(s)
Professional males who like a great haircut, wet shave and may consider a facial if in the right environment. Total pampering experience in a boys environment.
Industry/Entity Type
Barber
Contact Information for Business Card
Front- Logo - address is 42 Kowhai Rd Taupo
Ph - (07) 548 9163
www.ironvalebarbers.com
email - hello@ironvale.co.nz
Back of card
Mens Haircare - Wet Shaving - Facials - Skin Prescriptions
We are doing a loyalty program - 6 squares numbered then 7th free
Colors
Designer to choose colors to be used in the design.
Requirements
Must have
- Clean simple easy to read.
Nice to have
- Our current colours are white font on black background but thinking we need to introduce another colour. Maybe white logo on a copper, bronze or rusty background. Or even a rustic red brick wall with white writing. Want it clean simple to read. Maybe a burgundy?
Should not have
- no images like heads, scissors, razors please

```html
<!DOCTYPE html>
<html lang="en">
<head>
<meta charset="utf-8">
<title>Ironvale Barbers — Business Cards</title>
<link rel="stylesheet" href="https://fonts.googleapis.com/css2?family=Tinos:wght@400;700&display=swap">
<style>
  :root {
    --backdrop: #d6d6d6;
    --card: #262626;
    --ink: #ffffff;
    --shadow: rgba(0, 0, 0, 0.35);
  }
  * { margin: 0; padding: 0; box-sizing: border-box; }
  html, body {
    width: 1200px; height: 823px; overflow: hidden;
    background: var(--backdrop);
    font-family: "Tinos", "Times New Roman", serif;
    color: var(--ink);
  }
  .card {
    position: absolute; left: 278px; width: 576px; height: 338px;
    background: var(--card);
    box-shadow: 0 2px 6px var(--shadow);
  }
  .card--front { top: 40px; }
  .card--back { top: 419px; }

  .wordmark {
    position: absolute; left: 0; right: 0; text-align: center;
    font-weight: 700; line-height: 1; color: var(--ink);
  }
  .card--front .wordmark { top: 104px; }
  .card--front .wordmark__name { font-size: 62px; letter-spacing: 1px; }
  .card--front .wordmark__trade { font-size: 24px; letter-spacing: 9px; margin-top: 10px; }
  .card--back .wordmark { top: 74px; }
  .card--back .wordmark__name { font-size: 34px; letter-spacing: 1px; }
  .card--back .wordmark__trade { font-size: 14px; letter-spacing: 5px; margin-top: 6px; }

  .services {
    position: absolute; left: 120px; width: 340px; top: 242px;
    font-size: 14px; white-space: nowrap; text-align: center;
  }
  .services .dot { margin: 0 3px; font-weight: 700; }
  .appointment {
    position: absolute; left: 120px; width: 340px; top: 269px;
    font-size: 14px; display: flex; align-items: flex-end; white-space: nowrap;
  }
  .appointment .blank {
    display: inline-block; border-bottom: 1px solid var(--ink);
    height: 12px; margin: 0 4px;
  }
  .appointment .blank--date { width: 122px; }
  .appointment .blank--time { width: 136px; margin-right: 0; }

  .person {
    position: absolute; left: 0; right: 0; top: 177px; text-align: center;
  }
  .person__name { font-size: 21px; font-weight: 700; letter-spacing: 5px; line-height: 1; }
  .person__role { font-size: 13px; margin-top: 3px; }
  .divider {
    position: absolute; left: 38px; width: 514px; top: 232px;
    border-top: 1px solid var(--ink);
  }
  .contact {
    position: absolute; display: flex; align-items: center;
    font-size: 15px; white-space: nowrap;
  }
  .contact svg { width: 16px; height: 16px; margin-right: 8px; flex: none; }
  .contact--address { left: 77px; top: 251px; }
  .contact--phone { left: 77px; top: 282px; }
  .contact--email { left: 298px; top: 251px; letter-spacing: 1px; }
  .contact--web { left: 298px; top: 282px; }
</style>
</head>
<body>
  <section class="card card--front">
    <div class="wordmark">
      <div class="wordmark__name">IRONVALE</div>
      <div class="wordmark__trade">BARBERS</div>
    </div>
    <p class="services">Mens Haircare <span class="dot">.</span> Wet Shaving <span class="dot">.</span> Facials <span class="dot">.</span> Skin Prescriptions</p>
    <p class="appointment">Date -<span class="blank blank--date"></span>Time -<span class="blank blank--time"></span></p>
  </section>

  <section class="card card--back">
    <div class="wordmark">
      <div class="wordmark__name">IRONVALE</div>
      <div class="wordmark__trade">BARBERS</div>
    </div>
    <div class="person">
      <div class="person__name">YOUR NAME</div>
      <div class="person__role">Designation</div>
    </div>
    <div class="divider"></div>

    <div class="contact contact--address">
      <svg viewBox="0 0 16 16" aria-hidden="true"><circle cx="8" cy="8" r="7.3" fill="none" stroke="#fff" stroke-width="1.2"/><path d="M3.8 8.3 8 4.5l4.2 3.8M5.2 7.4v4h2v-2.4h1.6v2.4h2v-4" fill="none" stroke="#fff" stroke-width="1.2"/></svg>
      42 Kowhai Rd Taupo
    </div>
    <div class="contact contact--phone">
      <svg viewBox="0 0 16 16" aria-hidden="true"><circle cx="8" cy="8" r="7.3" fill="none" stroke="#fff" stroke-width="1.2"/><path d="M5.6 4.2c.4-.2.8 0 1 .4l.6 1.3c.1.3 0 .6-.2.8l-.5.4c.4.9 1.1 1.7 2 2.1l.4-.5c.2-.2.5-.3.8-.2l1.3.6c.4.2.6.6.4 1l-.3.7c-.2.4-.6.6-1 .6-2.9-.3-5.1-2.6-5.4-5.4 0-.4.2-.8.6-1z" fill="#fff"/></svg>
      +64 7 548 9163
    </div>
    <div class="contact contact--email">
      <svg viewBox="0 0 16 16" aria-hidden="true"><circle cx="8" cy="8" r="7.3" fill="none" stroke="#fff" stroke-width="1.2"/><rect x="4" y="5.3" width="8" height="5.4" fill="none" stroke="#fff" stroke-width="1.1"/><path d="M4 5.3 8 8.5l4-3.2" fill="none" stroke="#fff" stroke-width="1.1"/></svg>
      hello@ironvale.co.nz
    </div>
    <div class="contact contact--web">
      <svg viewBox="0 0 16 16" aria-hidden="true"><circle cx="8" cy="8" r="7.3" fill="none" stroke="#fff" stroke-width="1.2"/><circle cx="8" cy="8" r="4" fill="none" stroke="#fff" stroke-width="0.9"/><ellipse cx="8" cy="8" rx="1.7" ry="4" fill="none" stroke="#fff" stroke-width="0.9"/><path d="M4 8h8" stroke="#fff" stroke-width="0.9"/></svg>
      www.ironvalebarbers.com
    </div>
  </section>
</body>
</html>
```